We need our website look and feel updated to match our brand

We are looking to update our website and a "where to buy" tab at the top of the website. The current look and feel is ok but needs a clean up. The task is as follows:
1. Update the current pages and add a page for "Where to Buy"
2. Update the product page to reflect our current products. ie we have only three products now. Sublay K, Sublay M and SHEENIX. This page will have very similar descriptions and at the bottom of each product will be a link to our SDS (safety data sheets).
3. Please visit our current website for the look and feel.
4. Use our New Taglines need to be included. "Always Cleaning. All the Time." "24/7 SAFE SURFACE PROTECTION" (Logo as well)
5. The HomePage will need a nice clean location to our corporate video. https://clipvue.net/q7LrTn2WbXo (link for viewing) that will be the highlight and easy to access on the homepage.
Some examples of websites we like.
https://glimmerpad.com/
https://loftrovers.com/ (like the use of motion graphics in these)
Our focus claims are that our product is a surface cleaner and deodorizer. We would like to see variations in black, white background (Black header bar) and Gray backgrounds.

```html
<!DOCTYPE html>
<html lang="en">
<head>
<meta charset="utf-8">
<title>Veracoat — Website Design</title>
<link href="https://fonts.googleapis.com/css2?family=Montserrat:wght@400;500;600;700&family=Poppins:wght@300;400;500;600;700&display=swap" rel="stylesheet">
<style>
:root{
  --black:#050505;
  --ink:#0c0c0c;
  --gray:#777777;
  --gray-dark:#5e5e5e;
  --yellow:#ffcb08;
  --light:#f2f2f2;
  --white:#ffffff;
  --muted:#9a9a9a;
}
*{margin:0;padding:0;box-sizing:border-box}
html,body{width:1200px;height:3458px;overflow:hidden}
body{position:relative;background:var(--white);font-family:"Poppins",sans-serif;color:var(--black)}
.abs{position:absolute}

/* brand strip */
.brand-logo{left:309px;top:112px;display:flex;align-items:center;gap:8px}
.wordmark{font-family:"Poppins",sans-serif;font-weight:600;letter-spacing:-.3px}
.brand-logo .mark{width:22px;height:22px;background:var(--yellow)}
.brand-logo .wordmark{font-size:30px;color:var(--black)}
.divider{width:1px;height:84px;background:#d6d6d6;top:91px}
.strip-label{font-family:"Montserrat",sans-serif;font-size:22px;font-weight:400;color:var(--black)}
.font-name{font-size:18px;color:#333;line-height:22px}
.swatch{width:38px;height:38px;border-radius:50%;top:121px}
.hex{font-size:9px;color:#333;top:165px;width:50px;text-align:center}

/* flat screens */
.screen{overflow:hidden;box-shadow:0 18px 40px rgba(0,0,0,.18)}
.screen .mini{width:574px;height:353px;transform-origin:0 0;position:absolute;left:0;top:0}

/* shared page bits */
.page{left:313px;width:574px}
.topbar{height:16px;background:var(--black);border-bottom:1px solid #1d1d1d}
.topbar span{position:absolute;top:4px;font-size:5px;color:#cfcfcf;display:flex;align-items:center;gap:3px}
.topbar i{display:inline-block;width:4px;height:4px;background:var(--yellow);border-radius:50%}
.nav{height:54px;background:var(--black);border-bottom:1px solid #1d1d1d}
.nav-logo{left:76px;top:17px;display:flex;align-items:center;gap:4px}
.nav-logo .mark{width:10px;height:10px;background:var(--yellow)}
.nav-logo .wordmark{font-size:14px;color:var(--white)}
.menu{left:174px;top:24px;display:flex;gap:13px;font-size:5px;font-weight:500;color:#e6e6e6;letter-spacing:.2px}
.menu .active{color:var(--yellow);text-decoration:underline}
.nav .rule{left:522px;top:0;width:1px;height:54px;background:#222}
.nav .search{left:544px;top:23px}

.hero{height:351px;background:linear-gradient(165deg,#000 0%,#050505 45%,#2a2a2a 80%,#555 100%);overflow:hidden}
.hero-photo{left:304px;top:56px;width:270px;height:295px;background:radial-gradient(ellipse at 65% 30%,#e9e9e9 0%,#bdbdbd 14%,#3a3a3a 38%,rgba(40,40,40,0) 70%),linear-gradient(200deg,#111 0%,#555 70%,#777 100%)}
.hero-mist{left:0;top:200px;width:420px;height:151px;background:radial-gradient(ellipse at 70% 40%,rgba(170,170,170,.55),rgba(0,0,0,0) 65%)}
.eyebrow{font-size:5px;letter-spacing:2.6px;text-transform:uppercase;font-weight:500}
.hero .eyebrow{left:76px;top:97px;color:#cfcfcf}
.hero-title{left:76px;top:113px;font-size:22px;line-height:27px;font-weight:600;color:var(--white)}
.hero-title em{font-style:normal;color:var(--yellow)}
.btn{background:var(--yellow);color:var(--black);font-size:5px;font-weight:600;display:flex;align-items:center;justify-content:center;letter-spacing:.3px}
.hero .btn{left:76px;top:179px;width:63px;height:22px}

/* intro panel */
.intro{left:389px;top:1193px;width:422px;height:106px;background:var(--gray)}
.intro .eyebrow{left:26px;top:33px;color:#eee;font-size:4.5px;letter-spacing:1.6px}
.intro-title{left:26px;top:44px;font-size:14px;line-height:17px;font-weight:600;color:var(--yellow)}
.intro ul{list-style:none;left:180px;top:26px;width:230px}
.intro li{position:relative;font-size:4.6px;line-height:8px;color:#f4f4f4;padding-left:11px;margin-bottom:5px}
.intro li::before{content:"";position:absolute;left:0;top:1.5px;width:5px;height:5px;border-radius:50%;background:var(--yellow);box-shadow:0 0 0 1.5px rgba(255,203,8,.35)}

.section-light{background:var(--light)}
.section-dark{background:var(--black)}
.sec-label{font-size:5px;letter-spacing:2.6px;text-transform:uppercase;color:var(--muted)}
.section-dark .sec-label{color:var(--yellow);width:574px;text-align:center;left:0}
.sec-title{font-size:15px;font-weight:600}
.section-dark .sec-title{color:var(--white);width:574px;text-align:center;left:0}
.body-copy{font-size:4.8px;line-height:8.6px;color:#777}

/* about */
.about-photo{left:87px;top:101px;width:174px;height:221px;background:linear-gradient(150deg,#ffffff 0%,#f1f1f1 50%,#dcdcdc 100%);border:1px solid #e4e4e4}
.badge{left:76px;top:246px;width:90px;height:49px;background:var(--black);color:var(--yellow);font-size:6px;font-weight:600;text-align:center;display:flex;align-items:center;justify-content:center;line-height:8px}

/* products */
.product{width:132px}
.product-photo{width:132px;height:172px;border:1px solid #9a9a9a}
.product h3{font-size:6.5px;font-weight:600;color:var(--white);text-align:center;margin-top:13px}
.product p{font-size:4.4px;line-height:7.6px;color:#bdbdbd;text-align:center;margin-top:6px}
.product a{display:block;font-size:4.6px;color:var(--yellow);text-align:center;margin-top:10px;text-decoration:none;letter-spacing:.2px}

/* video */
.video{background:var(--gray);overflow:hidden}
.video-bg{left:0;top:70px;width:574px;height:118px;background:linear-gradient(180deg,rgba(119,119,119,0) 0%,rgba(150,150,150,.45) 60%,rgba(130,130,130,.25) 100%)}
.video-title{left:0;top:43px;width:574px;text-align:center;font-size:13.5px;font-weight:600;color:var(--white)}
.video-title em{font-style:normal;color:var(--yellow)}
.video-sub{left:0;top:78px;width:574px;text-align:center;font-size:4.8px;color:#e2e2e2}
.play{left:266px;top:99px}

/* care */
.tile{width:97px;display:flex;flex-direction:column;align-items:center;justify-content:center;text-align:center;gap:10px;padding:0 12px}
.tile p{font-size:4.4px;line-height:7.6px}
.tile.grey{background:var(--gray);color:#eee}
.tile.yellow{background:var(--yellow);color:#3b3b3b}

/* projects */
.project{overflow:hidden}
.caption{font-size:6px;color:#e5e5e5;text-align:center}
.caption b{color:var(--yellow);font-weight:400}

/* subscribe */
.subscribe{background:var(--yellow)}
.sub-title{left:76px;top:48px;font-size:14px;font-weight:600;color:var(--black)}
.sub-copy{left:76px;top:73px;font-size:4.8px;color:#6b5a10}
.email{left:328px;top:50px;width:141px;height:26px;border:1px solid var(--black);font-size:4.8px;color:#5a4a00;padding:10px 10px}
.send{left:469px;top:50px;width:29px;height:26px;background:var(--black);display:flex;align-items:center;justify-content:center}

/* footer */
.footer{background:var(--black)}
.foot-logo{left:76px;top:40px;display:flex;align-items:center;gap:4px}
.foot-logo .mark{width:10px;height:10px;background:var(--yellow)}
.foot-logo .wordmark{font-size:14px;color:var(--white)}
.foot-about{left:76px;top:84px;width:90px;font-size:4.6px;line-height:8px;color:#bdbdbd}
.foot-col h4{font-size:7.5px;font-weight:500;color:var(--white)}
.foot-col .line{width:16px;height:1px;background:var(--gray);margin:13px 0 10px}
.foot-col ul{list-style:none}
.foot-col li{font-size:4.8px;color:#d5d5d5;height:15.6px;display:flex;gap:4px;align-items:flex-start}
.foot-col li::before{content:"»";color:var(--gray)}
.foot-col.contact li::before{content:"";width:4px;height:4px;margin-top:1px;background:var(--yellow);border-radius:50%}
.copyright{background:var(--gray-dark);height:31px}
.copyright span{left:76px;top:12px;font-size:4.6px;color:#ececec}
</style>
</head>
<body>

<!-- brand strip -->
<div class="abs brand-logo"><span class="mark"></span><span class="wordmark">Veracoat</span></div>
<div class="abs divider" style="left:497px"></div>
<div class="abs strip-label" style="left:571px;top:88px">Fonts:</div>
<div class="abs font-name" style="left:571px;top:131px;font-family:'Montserrat',sans-serif">Gotham</div>
<div class="abs font-name" style="left:571px;top:154px;font-family:'Poppins',sans-serif">Poppins</div>
<div class="abs divider" style="left:717px"></div>
<div class="abs strip-label" style="left:792px;top:88px">Colors:</div>
<div class="abs swatch" style="left:792px;background:var(--black)"></div>
<div class="abs swatch" style="left:840px;background:var(--gray)"></div>
<div class="abs swatch" style="left:886px;background:var(--yellow)"></div>
<div class="abs hex" style="left:786px">#050505</div>
<div class="abs hex" style="left:834px">#777777</div>
<div class="abs hex" style="left:880px">#ffcb08</div>

<!-- flat hero screens -->
<div class="abs screen" style="left:463px;top:275px;width:611px;height:356px">
  <div class="mini" style="transform:scale(1.0645)">
    <div class="abs topbar" style="left:0;top:0;width:574px"><span style="left:377px"><i></i>Norwell, ME, USA</span><span style="left:434px"><i></i>hello@veracoat.net</span></div>
    <div class="abs nav" style="left:0;top:16px;width:574px">
      <div class="abs nav-logo"><span class="mark"></span><span class="wordmark">Veracoat</span></div>
      <div class="abs menu"><span class="active">HOME</span><span>ABOUT US</span><span>OUR PRODUCTS</span><span>OUR TECHNOLOGY</span><span>NEWS</span><span>FAQ</span><span>CONTACT</span><span>WHERE TO BUY</span></div>
    </div>
    <div class="abs hero" style="left:0;top:70px;width:574px">
      <div class="abs hero-mist"></div>
      <div class="abs hero-photo" role="img" aria-label="Hand holding a spray gun releasing a fine mist"></div>
      <div class="abs eyebrow" style="left:76px;top:97px;color:#cfcfcf">Welcome to Veracoat</div>
      <div class="abs hero-title">Always <em>Cleaning,</em><br>All The Time!</div>
      <div class="abs btn" style="left:76px;top:179px;width:63px;height:22px">READ MORE</div>
    </div>
  </div>
</div>
<div class="abs screen" style="left:168px;top:490px;width:382px;height:235px">
  <div class="mini" style="transform:scale(.6655)">
    <div class="abs topbar" style="left:0;top:0;width:574px"><span style="left:377px"><i></i>Norwell, ME, USA</span><span style="left:434px"><i></i>hello@veracoat.net</span></div>
    <div class="abs nav" style="left:0;top:16px;width:574px">
      <div class="abs nav-logo"><span class="mark"></span><span class="wordmark">Veracoat</span></div>
      <div class="abs menu"><span class="active">HOME</span><span>ABOUT US</span><span>OUR PRODUCTS</span><span>OUR TECHNOLOGY</span><span>NEWS</span><span>FAQ</span><span>CONTACT</span><span>WHERE TO BUY</span></div>
    </div>
    <div class="abs hero" style="left:0;top:70px;width:574px">
      <div class="abs hero-mist"></div>
      <div class="abs hero-photo" role="img" aria-label="Hand holding a spray gun releasing a fine mist"></div>
      <div class="abs eyebrow" style="left:76px;top:97px;color:#cfcfcf">Welcome to Veracoat</div>
      <div class="abs hero-title">Always <em>Cleaning,</em><br>All The Time!</div>
      <div class="abs btn" style="left:76px;top:179px;width:63px;height:22px">READ MORE</div>
    </div>
  </div>
</div>

<!-- full home page -->
<div class="abs page topbar" style="top:827px">
  <span style="left:377px"><i></i>Norwell, ME, USA</span>
  <span style="left:434px"><i></i>hello@veracoat.net</span>
</div>
<header class="abs page nav" style="top:843px">
  <div class="abs nav-logo"><span class="mark"></span><span class="wordmark">Veracoat</span></div>
  <nav class="abs menu"><span class="active">HOME</span><span>ABOUT US</span><span>OUR PRODUCTS</span><span>OUR TECHNOLOGY</span><span>NEWS</span><span>FAQ</span><span>CONTACT</span><span>WHERE TO BUY</span></nav>
  <div class="abs rule"></div>
  <svg class="abs search" width="9" height="9" viewBox="0 0 10 10"><circle cx="4" cy="4" r="3" fill="none" stroke="#ffcb08" stroke-width="1"/><line x1="6.3" y1="6.3" x2="9" y2="9" stroke="#ffcb08" stroke-width="1"/></svg>
</header>

<section class="abs page hero" style="top:897px">
  <div class="abs hero-mist"></div>
  <div class="abs hero-photo" role="img" aria-label="Hand holding a spray gun releasing a fine mist"></div>
  <div class="abs eyebrow">Welcome to Veracoat</div>
  <h1 class="abs hero-title">Always <em>Cleaning,</em><br>All The Time!</h1>
  <div class="abs btn">READ MORE</div>
</section>

<section class="abs page section-light" style="top:1248px;height:366px">
  <div class="abs about-photo" role="img" aria-label="Periodic table detail showing titanium with the product label"></div>
  <div class="abs badge">+20 YEARS<br>OF EXPERIENCE</div>
  <div class="abs sec-label" style="left:292px;top:101px">About us</div>
  <h2 class="abs sec-title" style="left:292px;top:116px">Real World Solution</h2>
  <p class="abs body-copy" style="left:292px;top:141px;width:206px">The onset of COVID-19 has changed our lives forever. The current methods of cleaning surfaces are not sustainable. Cleaning the environment we live in with liquids, UV-C light, ammonia-based cleaners and other harsh chemicals is wasteful. The moment you clean the surface and an infected person touches that surface again, it requires reapplication of your protective cleaners.</p>
  <p class="abs body-copy" style="left:292px;top:222px;width:206px">Veracoat is bringing a permanent surface coating formula to the United States market. A titanium dioxide photocatalyst coating that is incredibly long lasting and durable. How long? It basically lasts as long as the substrate is present. As long as it is not mechanically removed or painted over, it lasts for decades on any surface, indoor or outdoor.</p>
  <div class="abs btn" style="left:292px;top:298px;width:63px;height:22px">READ MORE</div>
</section>

<aside class="abs intro">
  <div class="abs eyebrow">Permanent surface cleaner</div>
  <h2 class="abs intro-title">What is Veracoat<br>Surface Protect?</h2>
  <ul class="abs">
    <li>Veracoat is a clear, long-lasting, fast-acting, self-cleaning surface coating.</li>
    <li>It safely protects surfaces keeping them cleaner, smelling better, and guarding anything it's applied to.</li>
    <li>Can be applied to both fabric and solid surfaces.</li>
  </ul>
</aside>

<section class="abs page section-dark" style="top:1614px;height:396px">
  <div class="abs sec-label" style="top:49px">What we offer</div>
  <h2 class="abs sec-title" style="top:64px">Veracoat Products</h2>
  <article class="abs product" style="left:76px;top:104px">
    <div class="product-photo" role="img" aria-label="White gallon jug of Sublay K" style="background:linear-gradient(180deg,#1d1d1d 0%,#cfcfcf 30%,#f3f3f3 60%,#2a2a2a 100%)"></div>
    <h3>Veracoat Sublay K</h3>
    <p>Veracoat Sublay K is applied on top of Veracoat Sublay M binder. The surface is a photocatalytic when exposed to sunlight.</p>
    <a>VIEW MORE DETAILS →</a>
  </article>
  <article class="abs product" style="left:221px;top:104px">
    <div class="product-photo" role="img" aria-label="Amber gallon jug of Sublay M" style="background:linear-gradient(180deg,#1d1d1d 0%,#e2c48a 30%,#f3d99a 60%,#2a2a2a 100%)"></div>
    <h3>Veracoat Sublay M</h3>
    <p>Veracoat Sublay K is applied on top of Veracoat Sublay M binder. Combined they form a permanent light activated titanium dioxide on all surfaces.</p>
    <a>VIEW MORE DETAILS →</a>
  </article>
  <article class="abs product" style="left:365px;top:104px">
    <div class="product-photo" role="img" aria-label="Yellow gallon jug of SHEENIX" style="background:linear-gradient(180deg,#1d1d1d 0%,#eed36a 30%,#f5df7c 60%,#2a2a2a 100%)"></div>
    <h3>SHEENIX</h3>
    <p>Veracoat SHEENIX is applied on top of the Sublay binder. Combined they form a permanent light activated titanium dioxide surface.</p>
    <a>VIEW MORE DETAILS →</a>
  </article>
</section>

<section class="abs page video" style="top:2010px;height:188px">
  <div class="abs video-bg" role="img" aria-label="Faint row of laboratory glass jars"></div>
  <h2 class="abs video-title">Veracoat is the World's Finest <em>Permanent Surface Cleaner</em></h2>
  <p class="abs video-sub">Check our video below to see how Veracoat works</p>
  <svg class="abs play" width="42" height="42" viewBox="0 0 42 42"><circle cx="21" cy="21" r="21" fill="#050505"/><path d="M17 14 L29 21 L17 28 Z" fill="#ffcb08"/></svg>
</section>

<section class="abs page section-light" style="top:2198px;height:345px">
  <div class="abs sec-label" style="left:76px;top:91px">Veracoat technology</div>
  <h2 class="abs sec-title" style="left:76px;top:106px">Care Instructions</h2>
  <p class="abs body-copy" style="left:76px;top:133px;width:172px">Veracoat is a photocatalyst that uses light, oxygen and water in the air to break down organic molecules that touch its surface. It works on increased molecules that cause smells or make surfaces dirty.</p>
  <p class="abs body-copy" style="left:76px;top:185px;width:172px">Large blob-like splashes on surfaces should be wiped away with a wet cloth to allow Veracoat Surface Protect to do the job. Veracoat prevents mold, mildew, algae and other contaminants.</p>
  <div class="abs btn" style="left:76px;top:236px;width:66px;height:21px">READ MORE</div>

  <div class="abs tile grey" style="left:292px;top:56px;height:114px">
    <svg width="26" height="26" viewBox="0 0 26 26" fill="none" stroke="#ffcb08" stroke-width="1.2"><rect x="6" y="4" width="14" height="9" rx="1" transform="rotate(-20 13 8)"/><path d="M6 16 L12 22 L20 14"/></svg>
    <p>Wipe surfaces with a soft wet Microfiber Cloth, Sponge or Paper towel</p>
  </div>
  <div class="abs tile yellow" style="left:292px;top:184px;height:115px">
    <svg width="26" height="26" viewBox="0 0 26 26" fill="none" stroke="#3b3b3b" stroke-width="1.2"><circle cx="13" cy="13" r="9"/><line x1="6.5" y1="6.5" x2="19.5" y2="19.5"/><path d="M9 14 L12 11 L16 15"/></svg>
    <p>Abrasive Pads or Tools not advised for surface cleaning</p>
  </div>
  <div class="abs tile yellow" style="left:400px;top:47px;height:117px">
    <svg width="26" height="26" viewBox="0 0 26 26" fill="none" stroke="#3b3b3b" stroke-width="1.2"><circle cx="9" cy="9" r="4"/><circle cx="17" cy="7" r="3"/><circle cx="16" cy="16" r="5"/><circle cx="7" cy="19" r="2"/></svg>
    <p>Use water or water and soap</p>
  </div>
  <div class="abs tile grey" style="left:400px;top:176px;height:116px">
    <svg width="26" height="26" viewBox="0 0 26 26" fill="none" stroke="#ffcb08" stroke-width="1.2"><path d="M11 3 C15 10 18 13 18 17 A7 7 0 0 1 4 17 C4 13 7 10 11 3 Z"/><circle cx="18" cy="18" r="4"/></svg>
    <p>Strong Chlorides, Acids or Bleaches on surfaces not essential anymore</p>
  </div>
</section>

<section class="abs page section-dark" style="top:2543px;height:487px">
  <div class="abs sec-label" style="top:50px">Recent work</div>
  <h2 class="abs sec-title" style="top:65px">Veracoat Projects</h2>
  <div class="abs project" role="img" aria-label="Bright hospital operating room" style="left:76px;top:101px;width:240px;height:142px;background:linear-gradient(160deg,#8fd6f0 0%,#4fb2d8 45%,#1d6f94 100%)"></div>
  <div class="abs caption" style="left:76px;top:259px;width:240px">University Hospital <b>→</b></div>
  <div class="abs project" role="img" aria-label="Fast food restaurant storefront at night" style="left:328px;top:101px;width:170px;height:142px;background:linear-gradient(170deg,#7a2a22 0%,#3a2a26 45%,#a88a64 100%)"></div>
  <div class="abs caption" style="left:328px;top:259px;width:170px">Burgerlane Volcano <b>→</b></div>
  <div class="abs project" role="img" aria-label="Toll booth counter comparing coated and non-coated sections" style="left:76px;top:279px;width:169px;height:142px;background:linear-gradient(170deg,#6b2a2a 0%,#8a8a8a 50%,#d7d7d7 100%)"></div>
  <div class="abs caption" style="left:76px;top:438px;width:169px">Toll Booth Test <b>→</b></div>
  <div class="abs project" role="img" aria-label="Clean public restroom with sinks and stalls" style="left:256px;top:279px;width:242px;height:142px;background:linear-gradient(170deg,#e9edf0 0%,#bfd0dc 50%,#5f86a8 100%)"></div>
  <div class="abs caption" style="left:256px;top:438px;width:242px">Odorless Bathrooms <b>→</b></div>
</section>

<section class="abs page subscribe" style="top:3030px;height:124px">
  <h2 class="abs sub-title">Subscribe for news updates</h2>
  <p class="abs sub-copy">Subscribe now to our mailing list to get the updates to your inbox</p>
  <div class="abs email">Your Email Address</div>
  <div class="abs send"><svg width="11" height="11" viewBox="0 0 12 12"><path d="M1 6 L11 1 L7 11 L5.5 7 Z" fill="#ffcb08"/></svg></div>
</section>

<footer class="abs page footer" style="top:3154px;height:181px">
  <div class="abs foot-logo"><span class="mark"></span><span class="wordmark">Veracoat</span></div>
  <p class="abs foot-about">Our US company was formed to take advantage of 20 years of experience with titanium dioxide in Japan. Our team is focused on real world solutions that are useful.</p>
  <div class="abs foot-col" style="left:217px;top:44px">
    <h4>Quick Links</h4><div class="line"></div>
    <ul><li>Home</li><li>About Us</li><li>FAQs</li><li>Contact</li></ul>
  </div>
  <div class="abs foot-col" style="left:320px;top:44px">
    <h4>Useful Links</h4><div class="line"></div>
    <ul><li>Our Products</li><li>Our Technology</li><li>News</li><li>Where to Buy?</li></ul>
  </div>
  <div class="abs foot-col contact" style="left:426px;top:44px">
    <h4>Contact</h4><div class="line"></div>
    <ul><li>hello@veracoat.net</li><li>Norwell, ME, USA</li></ul>
  </div>
</footer>
<div class="abs page copyright" style="top:3335px"><span class="abs">Copyright © 2020-2022 Veracoat, Inc.</span></div>

</body>
</html>
```